Business card and Stationery for data intelligence company

We need a new design for our business cards and stationery (Business Letter templates and a Quote example on Word, but it MUST work on Google Doc as well).

We are a software company based in Ireland and UK. Our product is "Quarla", data intelligence platform with beautiful visualizations, graph capabilities (things are interconnected), powerful, flexible, it can manage Big Data and Streaming information. It's modern and relatively open source.
Our company will provide data intelligence for law enforcements, pharmaceuticals, and similar high end customers.

We'll launch a new website soon. At the moment it's http://www.quarla.tech if you want to take a look. This is our youtube channel in case you need it to understand what Quarla is: https://www.youtube.com/c/quarlatechchannel

We changed the logo so please use the logo I attach here.

We'd like the output to be cool and modern but elegant and "business" at the same time. It should inspire simple sophistication, "unity" "intent" "purpose" yet subtly very advanced and innovative.

The name "Quarla" does NOT refer to sirens (mithological creatures) as well as the warning devices. It means Quantum Unified Archival Record Layer Array. Please use our logo's colors and if you want to something like the "graph" image.

```html
<!DOCTYPE html>
<html lang="en">
<head>
<meta charset="utf-8">
<title>Quarla Business Card</title>
<link href="https://fonts.googleapis.com/css2?family=Montserrat:wght@500&family=Open+Sans:wght@400;600&display=swap" rel="stylesheet">
<style>
  :root {
    --canvas-bg: #ecebe8;
    --brand-orange: #fbad3c;
    --card-white: #ffffff;
    --ink-dark: #2e2e2e;
    --ink-grey: #8c8c8c;
    --mark-faint-light: rgba(255, 255, 255, 0.16);
    --mark-faint-grey: rgba(120, 120, 120, 0.14);
  }
  * { box-sizing: border-box; margin: 0; padding: 0; }
  html, body { width: 1200px; height: 900px; overflow: hidden; }
  body {
    background: var(--canvas-bg);
    font-family: "Open Sans", Arial, sans-serif;
    position: relative;
  }
  .card {
    position: absolute;
    width: 560px;
    height: 320px;
    border-radius: 4px;
    overflow: hidden;
    box-shadow: 0 10px 28px rgba(0, 0, 0, 0.14);
  }
  .card-front { left: 90px; top: 90px; background: var(--brand-orange); }
  .card-back { left: 550px; top: 480px; background: var(--card-white); }

  .wordmark {
    font-family: "Montserrat", Arial, sans-serif;
    font-weight: 500;
    letter-spacing: 0.12em;
  }
  .front-brand {
    position: absolute;
    left: 120px; top: 108px;
    display: flex; align-items: center; gap: 20px;
  }
  .brand-dot {
    width: 76px; height: 76px; border-radius: 50%;
    border: 9px solid var(--card-white);
  }
  .front-brand .wordmark { color: var(--card-white); font-size: 48px; }
  .front-bg-mark {
    position: absolute; right: -40px; top: 20px;
    width: 250px; height: 250px; border-radius: 50%;
    border: 26px solid var(--mark-faint-light);
  }
  .social-row {
    position: absolute; left: 238px; top: 246px;
    display: flex; gap: 28px;
  }
  .social-slot {
    width: 20px; height: 20px; border-radius: 4px;
    background: var(--card-white);
  }

  .back-bg-mark {
    position: absolute; right: -30px; top: 40px;
    width: 240px; height: 240px; border-radius: 50%;
    border: 22px solid var(--mark-faint-grey);
  }
  .back-brand { position: absolute; left: 52px; top: 40px; }
  .back-brand .wordmark { color: var(--brand-orange); font-size: 44px; }
  .person { position: absolute; left: 52px; top: 128px; }
  .person-name { color: var(--brand-orange); font-weight: 600; font-size: 21px; line-height: 1.2; }
  .person-title { color: var(--ink-dark); font-size: 15px; margin-top: 2px; }
  .contact-list { position: absolute; left: 52px; top: 208px; list-style: none; }
  .contact-item {
    display: flex; align-items: center; gap: 12px;
    color: var(--ink-dark); font-size: 16px; line-height: 24px;
  }
  .contact-icon { width: 13px; height: 13px; fill: var(--brand-orange); flex: none; }
  .address {
    position: absolute; right: 26px; top: 150px;
    text-align: right; color: var(--ink-dark); font-size: 13px; line-height: 1.35;
  }
</style>
</head>
<body>

<section class="card card-front" aria-label="Card front">
  <div class="front-bg-mark"></div>
  <div class="front-brand">
    <div class="brand-dot"></div>
    <span class="wordmark">QUARLA</span>
  </div>
  <div class="social-row" aria-label="Social links">
    <span class="social-slot"></span>
    <span class="social-slot"></span>
    <span class="social-slot"></span>
  </div>
</section>

<section class="card card-back" aria-label="Card back">
  <div class="back-bg-mark"></div>
  <div class="back-brand"><span class="wordmark">QUARLA</span></div>
  <div class="person">
    <p class="person-name">Daniel Harlow</p>
    <p class="person-title">Managing Director</p>
  </div>
  <ul class="contact-list">
    <li class="contact-item">
      <svg class="contact-icon" viewBox="0 0 16 16" aria-hidden="true"><path d="M3 1h3l1.5 4-2 1.2a9 9 0 0 0 4.3 4.3L11 8.5l4 1.5v3a2 2 0 0 1-2 2A12 12 0 0 1 1 3a2 2 0 0 1 2-2z"/></svg>
      <span>123-456-7890</span>
    </li>
    <li class="contact-item">
      <svg class="contact-icon" viewBox="0 0 16 16" aria-hidden="true"><path d="M4 1h7v4H4z M1 6h14v8H1z"/><rect x="4" y="9" width="8" height="1.5" fill="#fff"/></svg>
      <span>123-456-7890</span>
    </li>
    <li class="contact-item">
      <svg class="contact-icon" viewBox="0 0 16 16" aria-hidden="true"><path d="M1 3h14v10H1z"/><path d="M1 3l7 6 7-6" fill="none" stroke="#fff" stroke-width="1.5"/></svg>
      <span>info@youremail.com</span>
    </li>
    <li class="contact-item">
      <svg class="contact-icon" viewBox="0 0 16 16" aria-hidden="true"><path d="M6.5 9.5l3-3" stroke="#fbad3c" stroke-width="2" fill="none"/><path d="M7 4l2-2a3 3 0 0 1 5 5l-2 2M9 12l-2 2a3 3 0 0 1-5-5l2-2" stroke="#fbad3c" stroke-width="2" fill="none"/></svg>
      <span>www.yourweb.com</span>
    </li>
  </ul>
  <address class="address" style="font-style: normal;">
    1234, Address Goes Here<br>
    Country Name, 123456
  </address>
</section>

</body>
</html>
```